Letterhead for New Orthopaedic Surgery Practice

My husband and I are starting our own practice named RB Spine & Vitality Center. We would like to create a nice simple but high class letterhead that doesn't use too much solid color ink when printing. I like the colors dark blue, gold, yellow. Open to other suggestions. We will need to list him and I both on the top of the letterhead. Here is the important information:
Lucinda Perrow, M.D. - Hand and Upper Extremity Surgery
Abena Quist, M.D. - Hip & Knee Replacement/General Orthopaedic Surgery
Location: 18735 North Harlow Pkwy
Maple Heights, FL 33498
Phone: 954-218-4650
Fax: 954-582-1346
Email: info@myrbspine.com

The only thing is that the phone and fax numbers will change once we get into our space. I just want to get the design started. I am including several documents which are my previous practice letterhead, my current procedure room letterhead, and our new Logo. The other letterheads are just for examples but please think outside of the box! We would love to see some great designs.

Colors
0054AA
0677BA
7BADD7
CADEEF
E8F1F8
0094D4
00A9DD
6FCCEA
C7EBF8
E9F6FB

Requirements
Must have
• class, elegance, luxury

```html
<!DOCTYPE html>
<html lang="en">
<head>
<meta charset="utf-8">
<title>RB Spine &amp; Vitality Center — Letterhead</title>
<link rel="stylesheet" href="https://fonts.googleapis.com/css2?family=Mulish:wght@400;600&display=swap">
<style>
  :root {
    --backdrop: #e6e6e8;
    --paper: #ffffff;
    --brand-blue: #27408b;
    --charcoal: #3a3a3c;
    --ink: #2b2b2e;
    --faint-mark: #dcdbe9;
    --on-band: #ffffff;
  }
  * { box-sizing: border-box; margin: 0; padding: 0; }
  html, body {
    width: 1014px; height: 1200px; overflow: hidden;
    background: var(--backdrop);
    font-family: "Mulish", "Helvetica Neue", Arial, sans-serif;
  }
  .letterhead {
    position: absolute; left: 57px; top: 17px;
    width: 900px; height: 1165px;
    background: var(--paper);
    box-shadow: 0 2px 10px rgba(0,0,0,0.12);
  }
  .masthead {
    position: absolute; left: 80px; top: 76px;
    display: flex; align-items: center; height: 110px;
  }
  .brand-name {
    width: 340px;
    display: flex; align-items: center; gap: 16px;
    color: var(--brand-blue);
    font-weight: 600; font-size: 27px; line-height: 1.15;
    letter-spacing: 0.5px; text-transform: uppercase;
  }
  .brand-square {
    width: 22px; height: 22px; background: var(--brand-blue); flex: none;
  }
  .masthead-divider {
    width: 2px; height: 100px; background: var(--brand-blue);
    margin: 0 62px 0 30px;
  }
  .physicians {
    color: var(--brand-blue); font-size: 15px; line-height: 19px;
    white-space: nowrap;
  }
  .physician-name { color: var(--ink); }
  .physician--first {
    border-bottom: 1.5px solid var(--brand-blue);
    padding-bottom: 4px; margin-bottom: 6px; width: 258px;
  }
  .watermark {
    position: absolute; left: 240px; top: 470px; width: 420px;
    display: flex; align-items: center; justify-content: center;
    color: var(--faint-mark);
    font-weight: 600; font-size: 52px; line-height: 1.1;
    text-transform: uppercase; text-align: left;
  }
  .footer-band {
    position: absolute; left: 0; bottom: 0; width: 100%; height: 90px;
    display: flex;
  }
  .footer-cell {
    width: 50%; display: flex; flex-direction: column;
    justify-content: center; align-items: center;
    color: var(--on-band); font-size: 16px; line-height: 21px;
  }
  .footer-address { background: var(--brand-blue); }
  .footer-contact { background: var(--charcoal); }
</style>
</head>
<body>
  <main class="letterhead">
    <header class="masthead">
      <div class="brand-name"><span class="brand-square"></span><span>RB Spine &amp;<br>Vitality Center</span></div>
      <div class="masthead-divider"></div>
      <div class="physicians">
        <div class="physician physician--first">
          <div class="physician-name">Lucinda Perrow, M.D.</div>
          <div class="physician-specialty">Hand and Upper Extremity Surgery</div>
        </div>
        <div class="physician">
          <div class="physician-name">Abena Quist, M.D.</div>
          <div class="physician-specialty">Hip &amp; Knee Replacement/General<br>Orthopaedic Surgery</div>
        </div>
      </div>
    </header>

    <div class="watermark" aria-hidden="true"><span>RB Spine &amp;<br>Vitality<br>Center</span></div>

    <footer class="footer-band">
      <div class="footer-cell footer-address">
        <span>18735 North Harlow Pkwy</span>
        <span>Maple Heights, FL 33498</span>
      </div>
      <div class="footer-cell footer-contact">
        <span>Fax: 954-582-1346</span>
        <span>Email: info@myrbspine.com</span>
      </div>
    </footer>
  </main>
</body>
</html>
```